Cravo Azul - Apresentação de nova plataforma de bilhética

Precisamos de uma apresentação do novo negócio para diferentes targets. Anexo briefing, logo e imagens tipo a usar.

```html
<!DOCTYPE html>
<html lang="pt">
<head>
<meta charset="utf-8">
<title>Cravo Azul — Apresentação</title>
<link href="https://fonts.googleapis.com/css2?family=Source+Serif+4:wght@600;700&family=Open+Sans:wght@400;600;700&display=swap" rel="stylesheet">
<style>
:root{
  --page:#e8e9eb;
  --navy:#1b1b2f;
  --navy-card:#2a2a3f;
  --red:#e8432c;
  --red-soft:#fde6e2;
  --red-light:#ed6450;
  --white:#ffffff;
  --off:#f6f6f7;
  --ink:#1b1b2f;
  --muted:#6b6f80;
  --serif:"Source Serif 4", Georgia, serif;
  --sans:"Open Sans", Arial, sans-serif;
}
*{margin:0;padding:0;box-sizing:border-box}
html,body{width:1200px;height:722px;overflow:hidden;background:var(--page);font-family:var(--sans);color:var(--ink)}
.deck{position:relative;width:1200px;height:722px}
.slide{position:absolute;width:377px;height:212px;overflow:hidden}
.abs{position:absolute}
.c{left:0;right:0;text-align:center}
.serif{font-family:var(--serif);font-weight:700}
.brand{display:flex;align-items:center;gap:6px;font-family:var(--sans);font-weight:700;color:var(--white)}
.brand-mark{width:14px;height:14px;background:var(--red);border-radius:2px}

/* hero */
.hero{left:16px;top:24px;background:var(--navy)}
.hero-photo{inset:0;background:radial-gradient(ellipse at 50% 10%,#7a4a3a 0%,#3a2f3f 40%,#1c1a2a 100%)}
.hero-shade{inset:0;background:linear-gradient(180deg,rgba(27,27,47,.25),rgba(27,27,47,.75))}
.hero .brand{left:0;right:0;top:54px;justify-content:center;font-size:20px}
.hero-tag{top:92px;font-size:10.5px;color:var(--white)}
.btn{background:var(--red);color:var(--white);font-weight:700;display:flex;align-items:center;justify-content:center;border-radius:2px}
.hero-btn{left:132px;top:113px;width:113px;height:24px;font-size:9px}
.hero-sub{top:150px;font-size:7px;color:#e6e6ec}
.hero-foot{top:180px;font-size:5.5px;color:#cfd0da}

/* about */
.about{left:412px;top:24px;background:var(--white)}
.about-side{left:0;top:0;width:158px;height:212px;background:var(--navy)}
.about-side .brand{left:0;right:0;top:90px;justify-content:center;font-size:18px}
.about-note{left:15px;top:141px;font-size:7.5px;line-height:11.5px;color:#c9cad6}
.about-title{left:173px;top:20px;font-size:13px}
.feat{left:174px;width:195px}
.feat-icon{position:absolute;left:0;top:-2px;width:12px;height:12px}
.feat h4{margin-left:20px;font-size:5.5px;font-weight:700}
.feat p{margin-left:20px;margin-top:10px;font-size:4.5px;color:var(--muted)}

/* events */
.events{left:807px;top:24px;background:var(--off)}
.events-title{top:15px;font-size:14px}
.events-sub{top:40px;font-size:5px;color:var(--muted)}
.photo{width:120px;height:66px;border-radius:10px;overflow:hidden}
.photo span{position:absolute;bottom:2px;left:0;right:0;text-align:center;font-size:5px;font-weight:700;color:var(--white)}

/* who */
.who{left:16px;top:256px;background:var(--white)}
.who-title{top:14px;font-size:14px}
.who-sub{top:39px;font-size:5.5px;color:var(--muted)}
.card{width:105px;height:57px;background:var(--white);border-radius:3px;box-shadow:0 1px 4px rgba(0,0,0,.1)}
.card.dark{background:var(--navy)}
.card .ico{position:absolute;left:8px;top:8px;width:20px;height:20px;border-radius:50%;background:var(--red-soft)}
.card.dark .ico{background:var(--red)}
.card .ico svg{position:absolute;left:4px;top:4px}
.card b{position:absolute;left:36px;top:24px;font-size:5.5px;line-height:7px}
.card.dark b{color:var(--white)}

/* how */
.how{left:412px;top:256px;background:var(--navy);color:var(--white)}
.how-title{top:14px;font-size:14px}
.how-sub{top:39px;font-size:5.5px;color:#b9bacb}
.step{width:80px;margin-left:-40px;text-align:center}
.step-num{width:38px;height:38px;margin:0 auto;border-radius:50%;background:var(--red);font-family:var(--serif);font-weight:700;font-size:13px;display:flex;align-items:center;justify-content:center}
.step h4{margin-top:9px;font-size:6px;font-weight:700}
.step p{margin-top:12px;font-size:4.3px;color:#b9bacb;line-height:5.5px}
.dash{top:80px;width:16px;height:1.5px;background:var(--red)}
.how-btn{left:120px;top:173px;width:136px;height:26px;font-size:6px}

/* promoters */
.promo{left:807px;top:256px;background:var(--white)}
.promo-photo{left:0;top:0;width:169px;height:212px;background:radial-gradient(ellipse at 60% 15%,#6d4a52 0%,#3a3040 45%,#1f1e2a 100%)}
.promo-head{left:16px;top:74px;font-size:15px;line-height:19px;color:var(--white)}
.promo-title{left:185px;top:21px;width:180px;font-size:9px;line-height:11px}
.bullet{left:181px;font-size:6px;display:flex;align-items:center;gap:9px}
.bullet i{width:8px;height:8px;border-radius:50%;background:var(--red)}
.promo-foot{left:181px;top:192px;width:169px;height:10px;background:var(--red-soft);color:var(--red);font-size:4.3px;display:flex;align-items:center;justify-content:center}

/* clients */
.clients{left:16px;top:487px;background:var(--navy);color:var(--white)}
.clients-title{top:14px;font-size:14px}
.quote{background:var(--navy-card);border-radius:4px;display:flex;align-items:center;padding-left:15px;font-family:var(--serif);font-weight:700;font-size:7px;line-height:8.5px}
.quote::before{content:"";position:absolute;left:6px;top:4px;bottom:4px;width:1.5px;background:var(--red)}

/* closing */
.close{left:412px;top:487px;background:var(--red);color:var(--white)}
.close .brand{left:24px;top:46px;font-size:17px}
.close .brand-mark{background:var(--white)}
.close-head{left:23px;top:89px;font-size:13.5px;line-height:16.5px}
.close-sub{left:23px;top:160px;font-size:7px;color:#fbd9d3}
.close-btn{left:19px;top:183px;width:113px;height:20px;background:var(--navy);font-size:6px;gap:4px}
.close-art{left:226px;top:40px;width:132px;height:88px;border-radius:8px;background:var(--red-light)}
</style>
</head>
<body>
<main class="deck">

  <section class="slide hero">
    <div class="abs hero-photo" role="img" aria-label="Fotografia de festa popular noturna com bandeirinhas coloridas e multidão"></div>
    <div class="abs hero-shade"></div>
    <div class="abs brand"><span class="brand-mark"></span>Cravo Azul</div>
    <p class="abs c hero-tag">Venda os seus ingressos online</p>
    <div class="abs btn hero-btn">GRÁTIS</div>
    <p class="abs c hero-sub">Simples. Rápido. Sem complicações.</p>
    <p class="abs c hero-foot">A plataforma portuguesa de bilhética para pequenos e médios eventos.</p>
  </section>

  <section class="slide about">
    <div class="abs about-side">
      <div class="abs brand"><span class="brand-mark"></span>Cravo Azul</div>
      <p class="abs about-note">A bilhética<br>simples para<br>Ptg.</p>
    </div>
    <h2 class="abs serif about-title">O que é o Cravo Azul?</h2>
    <div class="abs feat" style="top:50px">
      <svg class="feat-icon" viewBox="0 0 12 12"><circle cx="6" cy="6" r="6" fill="#e8432c"/><path d="M3.2 6.2l2 2 3.6-4" stroke="#fff" stroke-width="1.4" fill="none"/></svg>
      <h4>100% Gratuito para promotores</h4><p>Comece a vender bilhetes sem qualquer custo inicial.</p>
    </div>
    <div class="abs feat" style="top:89px">
      <svg class="feat-icon" viewBox="0 0 12 12"><path d="M7 0L2 7h3l-1 5 5-7H6z" fill="#e8432c"/></svg>
      <h4>Criação em minutos</h4><p>Crie o seu evento e comece logo a vender. Simples e rápido.</p>
    </div>
    <div class="abs feat" style="top:129px">
      <svg class="feat-icon" viewBox="0 0 12 12"><rect x="1.5" y="5" width="9" height="7" rx="1" fill="#e8432c"/><path d="M3.5 5V3.5a2.5 2.5 0 015 0V5" stroke="#e8432c" stroke-width="1.3" fill="none"/></svg>
      <h4>Pagamentos seguros</h4><p>Receba pagamentos de forma simples, rápida e segura.</p>
    </div>
    <div class="abs feat" style="top:169px">
      <svg class="feat-icon" viewBox="0 0 12 12"><rect x="3" y="0" width="6.5" height="12" rx="1.2" stroke="#e8432c" stroke-width="1.2" fill="none"/><circle cx="6.25" cy="10" r=".7" fill="#e8432c"/></svg>
      <h4>Acessível em qualquer dispositivo</h4><p>Plataforma otimizada para mobile e desktop.</p>
    </div>
  </section>

  <section class="slide events">
    <h2 class="abs c serif events-title">Para todos os tipos de eventos</h2>
    <p class="abs c events-sub">Música • Teatro • Cinema • Comédia • Festas • Workshops • Conferências • Feiras</p>
    <div class="abs photo" style="left:66px;top:57px;background:linear-gradient(160deg,#4a3424,#1d140e)" role="img" aria-label="Fotografia de elenco de teatro em palco"><span>Teatro &amp; Cinema</span></div>
    <div class="abs photo" style="left:198px;top:57px;background:linear-gradient(160deg,#b0266a,#2a1030)" role="img" aria-label="Fotografia de palco com luzes rosa e artista"><span>Comédia &amp; Música</span></div>
    <div class="abs photo" style="left:66px;top:133px;background:linear-gradient(160deg,#1f6fb8,#0d2350)" role="img" aria-label="Fotografia de auditório de conferência com ecrã"><span>Workshops &amp; Conferências</span></div>
    <div class="abs photo" style="left:198px;top:133px;background:linear-gradient(160deg,#6f7d5a,#3c4436)" role="img" aria-label="Fotografia de feira ao ar livre com tendas e visitantes"><span>Festas &amp; Feiras</span></div>
  </section>

  <section class="slide who">
    <h2 class="abs c serif who-title">Quem usa o Cravo Azul?</h2>
    <p class="abs c who-sub">Desenhado para pequenos e médios promotores em Portugal</p>
    <div class="abs card" style="left:19px;top:58px"><span class="ico"><svg width="12" height="12" viewBox="0 0 12 12"><circle cx="6" cy="4" r="2" fill="#e8432c"/><circle cx="2.5" cy="5" r="1.4" fill="#e8432c"/><circle cx="9.5" cy="5" r="1.4" fill="#e8432c"/><path d="M2 11a4 4 0 018 0z" fill="#e8432c"/></svg></span><b>Pequenas Autarquias</b></div>
    <div class="abs card" style="left:134px;top:58px"><span class="ico"><svg width="12" height="12" viewBox="0 0 12 12"><circle cx="6" cy="6" r="5" stroke="#e8432c" stroke-width="1.2" fill="none"/><path d="M1 6h10M6 1c-2.5 3-2.5 7 0 10M6 1c2.5 3 2.5 7 0 10" stroke="#e8432c" stroke-width="1" fill="none"/></svg></span><b>Coletividades</b></div>
    <div class="abs card" style="left:249px;top:58px"><span class="ico"><svg width="12" height="12" viewBox="0 0 12 12"><path d="M1 1v10h10" stroke="#e8432c" stroke-width="1.2" fill="none"/><path d="M3 8l2.5-3 2 2L11 3" stroke="#e8432c" stroke-width="1.2" fill="none"/></svg></span><b>Associações</b></div>
    <div class="abs card" style="left:19px;top:126px"><span class="ico"><svg width="12" height="12" viewBox="0 0 12 12"><rect x="3" y="0.5" width="6" height="11" rx="1" stroke="#e8432c" stroke-width="1.2" fill="none"/></svg></span><b style="top:20px">Teatros e Cinemas<br>Locais</b></div>
    <div class="abs card" style="left:134px;top:126px"><span class="ico"><svg width="12" height="12" viewBox="0 0 12 12"><path d="M7 0L2 7h3l-1 5 5-7H6z" fill="#e8432c"/></svg></span><b>Promotores Culturais</b></div>
    <div class="abs card dark" style="left:249px;top:126px"><span class="ico"><svg width="12" height="12" viewBox="0 0 12 12"><rect x="0.8" y="2.5" width="10.4" height="7" rx="1.2" stroke="#fff" stroke-width="1.2" fill="none"/><rect x="3" y="4.3" width="6" height="3.4" fill="#fff"/></svg></span><b>Eventos Universitários</b></div>
  </section>

  <section class="slide how">
    <h2 class="abs c serif how-title">Como funciona?</h2>
    <p class="abs c how-sub">Criar eventos nunca foi tão simples</p>
    <div class="abs step" style="left:54px;top:60px"><div class="step-num">1</div><h4>Crie o evento</h4><p>Em minutos, sem burocracia.</p></div>
    <div class="abs dash" style="left:90px"></div>
    <div class="abs step" style="left:141px;top:60px"><div class="step-num">2</div><h4>Partilhe online</h4><p style="margin-top:9px">Link direto para a sua<br>bilheteira.</p></div>
    <div class="abs dash" style="left:177px"></div>
    <div class="abs step" style="left:228px;top:60px"><div class="step-num">3</div><h4>Receba pagamentos</h4><p>Forma simples e segura.</p></div>
    <div class="abs dash" style="left:263px"></div>
    <div class="abs step" style="left:314px;top:60px"><div class="step-num">4</div><h4>Veja os resultados</h4><p>Controle tudo em tempo real.</p></div>
    <div class="abs btn how-btn">O palco é teu. A bilheteira é nossa.</div>
  </section>

  <section class="slide promo">
    <div class="abs promo-photo" role="img" aria-label="Fotografia de arraial noturno com bandeirinhas e multidão"></div>
    <h2 class="abs serif promo-head">Para<br>Promotores</h2>
    <h3 class="abs serif promo-title">A sua bilheteira online, gratuita e sem complicações.</h3>
    <p class="abs bullet" style="top:55px"><i></i>Comece a vender bilhetes grátis</p>
    <p class="abs bullet" style="top:83px"><i></i>Crie o evento e comece logo a vender</p>
    <p class="abs bullet" style="top:112px"><i></i>Receba pagamentos de forma simples e segura</p>
    <p class="abs bullet" style="top:140px"><i></i>Criar eventos nunca foi tão simples</p>
    <p class="abs bullet" style="top:168px"><i></i>Receba pagamentos rapidamente</p>
    <div class="abs promo-foot">Venda bilhetes online sem complicações → cravoazul.pt</div>
  </section>

  <section class="slide clients">
    <h2 class="abs c serif clients-title">Para os teus clientes</h2>
    <div class="abs quote" style="left:15px;top:49px;width:173px;height:56px">"O teu bilhete<br>para todos os momentos."</div>
    <div class="abs quote" style="left:197px;top:49px;width:165px;height:56px">"Hoje sais de casa."</div>
    <div class="abs quote" style="left:15px;top:113px;width:75px;height:48px">"Reserva já."</div>
    <div class="abs quote" style="left:98px;top:113px;width:75px;height:48px">"Vive já."</div>
    <div class="abs quote" style="left:181px;top:113px;width:87px;height:48px">"Descobre já."</div>
    <div class="abs quote" style="left:276px;top:113px;width:86px;height:48px">"Acontece já."</div>
  </section>

  <section class="slide close">
    <div class="abs brand"><span class="brand-mark"></span>Cravo Azul</div>
    <h2 class="abs serif close-head">A plataforma portuguesa<br>de bilhética simples,<br>rápida e sem complicações.</h2>
    <p class="abs close-sub">Para pequenos e médios eventos em Portugal.</p>
    <div class="abs btn close-btn">Crie o seu evento em minutos
      <svg width="7" height="6" viewBox="0 0 7 6"><path d="M0 3h6M4 1l2 2-2 2" stroke="#fff" stroke-width="1" fill="none"/></svg>
    </div>
    <div class="abs close-art" role="img" aria-label="Ilustração decorativa de um bilhete"></div>
  </section>

</main>
</body>
</html>
```